Etiketten für Freunde Bier gesucht
Zielgruppe
Wir engagieren uns ehrenamtlich für Kinder in Afrika.
In Einsatz-Teams von freiwilligen Helfern, sammeln wir während 8 Monaten Spendengelder, um Kindern in Townships's Südafrikas eine Zukunft zu bauen, in dem wir nicht staatliche Kindertagesstätten engagierter einheimischer Frauen umbauen.
Vorher bestehen die KITA's nur aus rostigen Wellblechhütten, welche nicht isoliert sind und auf dem KITA Gelände befindet sich weder Rasen, noch ein Spielplatz.
Aufgabenstellung
Um Spenden zu sammeln, möchten wir ein Freunde Bier auf den Markt bringen.
Infos zu den Maßen der Etiketten: Sie sollten nicht breiter als 8 cm sein. Wichtig ist, dass sich in der Ecke links oben keine Angaben befinden, da die obere linke Kante schräg nach oben verlaufen wird. Welche Angaben müssen zwingend auf den Etiketten zu finden sein?
Die Promill-Angaben (5.2% VOL)
Inhalts-Angabe (33cl) das Logo des Bierherstellers sollte auch mit auf die Etikette (nicht all zu gross) (siehe Bild Nr.2)
Die Info's zum Bier (Biersorte: Tannfelsbräu ORIGINAL)
Der Name des Bier's sollte Freunde Bier sein.
Wir möchten auf der Etikette auch folgendes unbedingt vermerken:
'Diese Flache (Bier) füllt 10 Breischalen für Kinder in Afrika'
Ansonsten haben wir überhaupt keine Vorstellung, was wir wörtlich noch auf die Etikette packen möchten (vielleicht fällt euch ja noch was tolles ein:-)
Was wir uns vom Design her so vorstellen:
Ich habe noch 3 Bilder (siehe Bild 3-4) dazugefügt, mit Designs, welche mir auf Anhieb sehr sehr gut gefallen (damit ihr einen Anhaltspunkt habt:-) Aber ich lasse mich auch gerne von anderen Design-Formen überraschen.

```html
<!DOCTYPE html>
<html lang="de">
<head>
<meta charset="utf-8">
<title>Freunde Bier – Etiketten</title>
<link rel="stylesheet" href="https://fonts.googleapis.com/css2?family=Bebas+Neue&family=Oswald:wght@400;500&display=swap">
<style>
  :root {
    --bg: #ececec;
    --teal: #6dd6d4;
    --white: #ffffff;
  }
  html, body {
    margin: 0;
    padding: 0;
    width: 1200px;
    height: 960px;
    overflow: hidden;
    background: var(--bg);
  }
  .canvas {
    position: relative;
    width: 1200px;
    height: 960px;
  }
  .neck-label {
    position: absolute;
    left: 270px;
    top: 103px;
    width: 128px;
    height: 416px;
  }
  .main-label {
    position: absolute;
    left: 458px;
    top: 103px;
    width: 472px;
    height: 754px;
  }
  .headline {
    font-family: "Bebas Neue", "Oswald", sans-serif;
  }
  .small-copy {
    font-family: "Oswald", sans-serif;
    font-weight: 400;
  }
  .brand-name {
    font-family: "Oswald", sans-serif;
    font-weight: 500;
  }
</style>
</head>
<body>
<main class="canvas">

  <svg class="neck-label" viewBox="0 0 128 416" aria-label="Halsetikette Freunde Bier">
    <polygon points="0,0 128,0 128,380 0,416" fill="var(--white)" stroke="var(--teal)" stroke-width="3"/>
    <rect x="0" y="0" width="128" height="132" fill="var(--teal)"/>
    <circle class="neck-disc" cx="64" cy="64" r="44" fill="var(--white)"/>
    <text class="headline" x="64" y="226" text-anchor="middle" font-size="40" fill="var(--teal)" textLength="104" lengthAdjust="spacingAndGlyphs">FREUNDE</text>
    <text class="headline" x="64" y="282" text-anchor="middle" font-size="66" fill="var(--teal)" textLength="92" lengthAdjust="spacingAndGlyphs">BIER</text>
    <polygon class="bookmark" points="52,300 76,300 76,334 64,324 52,334" fill="var(--teal)"/>
  </svg>

  <svg class="main-label" viewBox="0 0 472 754" aria-label="Hauptetikette Freunde Bier">
    <polygon class="label-shape" points="0,156 472,0 472,754 0,754" fill="var(--teal)"/>

    <text class="brand-name" x="454" y="100" text-anchor="end" font-size="24" fill="var(--white)">Tannfelsbräu</text>

    <text class="headline" x="8" y="336" font-size="228" fill="var(--white)" textLength="456" lengthAdjust="spacingAndGlyphs">FREUNDE</text>
    <text class="headline" x="8" y="524" font-size="228" fill="var(--white)" textLength="288" lengthAdjust="spacingAndGlyphs">BIER</text>

    <circle class="disc" cx="388" cy="436" r="66" fill="var(--white)"/>

    <line x1="8" y1="542" x2="464" y2="542" stroke="var(--white)" stroke-width="4"/>
    <line x1="274" y1="546" x2="274" y2="750" stroke="var(--white)" stroke-width="4"/>

    <g class="pennant" fill="var(--white)">
      <polygon points="206,568 262,568 262,580 218,580"/>
      <polygon points="206,586 262,586 262,600 218,600"/>
    </g>

    <g class="small-copy" font-size="16" fill="var(--white)">
      <text x="284" y="584">DER KAUF DIESER FLASCHE</text>
      <text x="284" y="608">BIER FÜLLT 10 MAIS BREI-</text>
      <text x="284" y="632">SCHALEN FÜR KINDER</text>
      <text x="284" y="656">IN AFRIKA. DANKE!</text>
    </g>

    <g class="small-copy" font-size="20" fill="var(--white)">
      <text x="10" y="732">5,2 % VOL</text>
      <text x="248" y="732" text-anchor="end">33 cl</text>
    </g>
  </svg>

</main>
</body>
</html>
```